The Tidegrove Newsletter For My Monthly Investment Newsletters

I'm looking to create two beautiful newsletter template for my new financial planning and investment firm. I keep my newsletters short and sweet as I feel less is more. One newsletter is for investment updates - I send that to clients and prospects. The other is more of an update for clients only.

I'm going to be using Mailchimp & Constant Contact so please make sure I can use that template there.

My newsletter typically goes out monthly. There are two versions - one for clients and one for prospects. Sometimes, information is applicable for clients only.

The newsletter brief should have the month and year in it like
The Tidegrove Newsletter: March 2020.

The other can be

The Tidegrove Update: March 2020 (for more administrative announcements).

Target Market(s)

Investors

Industry/Entity Type

Investment Advisory

Font styles to use
Sans Serif

Colors

Designer to choose colors to be used in the design.

Requirements
Must have
• Clean
• professional
• Modern feel
• Less is more.
• Colors should match and be in sync my logo.
• I'm going to be using Mailchimp & Constant Contact so please make sure I can use that template there.
Nice to have
• Please follow the must haves

```html
<!DOCTYPE html>
<html lang="en">
<head>
<meta charset="utf-8">
<title>The Tidegrove Newsletter Templates</title>
<link rel="stylesheet" href="https://fonts.googleapis.com/css2?family=Cinzel:wght@700&family=Roboto:wght@300;400;500;700&display=swap">
<style>
:root{
  --canvas:#c8c8c8;
  --teal:#1fb0bc;
  --deep-teal:#0e3f5c;
  --ink:#0b1f2a;
  --navy:#133f6b;
  --orange:#e07a1a;
  --bright-orange:#f57e20;
  --body:#3b3b3b;
  --white:#ffffff;
}
*{margin:0;padding:0;box-sizing:border-box}
html,body{width:1200px;height:1145px;overflow:hidden;background:var(--canvas);font-family:'Roboto',sans-serif}
.canvas{position:relative;width:1200px;height:1145px}
.newsletter{position:absolute;top:33px;overflow:hidden;background:var(--white)}
.newsletter--prospects{left:45px;width:547px;height:1050px}
.newsletter--clients{left:623px;width:535px;height:1054px}
.abs{position:absolute}

/* brand */
.brand{position:absolute;left:0;right:0;display:flex;justify-content:center;align-items:center;gap:12px;font-family:'Cinzel',serif;font-weight:700;font-size:34px;letter-spacing:1px}
.brand-dot{width:40px;height:40px;border-radius:50%}
.headline{position:absolute;left:0;right:0;text-align:center;font-family:'Cinzel',serif;font-weight:700;line-height:1.1}
.date-pill{position:absolute;border-radius:30px;display:flex;align-items:center;justify-content:center;font-family:'Cinzel',serif;font-weight:700;color:var(--white)}

/* prospects */
.hero-dark{left:0;top:0;width:547px;height:346px;background:linear-gradient(180deg,#0d3a56 0%,#14506a 55%,#1a5a6f 100%)}
.newsletter--prospects .brand{top:36px;color:var(--white)}
.newsletter--prospects .brand-dot{background:var(--white)}
.newsletter--prospects .headline{top:172px;font-size:37px;color:var(--white)}
.newsletter--prospects .date-pill{left:171px;top:257px;width:205px;height:53px;background:var(--teal);font-size:21px}
.hero-notch{left:253px;top:345px}
.features-bg{left:0;top:366px;width:547px;height:334px;background:linear-gradient(160deg,#f7f7f7 0%,#ececec 60%,#e2e2e2 100%)}
.feature-pin{position:absolute}
.feature{position:absolute;width:150px;text-align:center}
.feature h3{font-weight:700;font-size:15.5px;color:#111;letter-spacing:.2px}
.feature p{margin-top:8px;font-size:10.5px;line-height:14.7px;color:var(--body)}
.photo-field{left:0;top:700px;width:547px;height:350px;background:linear-gradient(160deg,#d9a98a 0%,#e9b46a 35%,#c98d2e 65%,#9a7a1e 100%)}
.service-card{left:136px;top:768px;width:300px;height:196px;border-radius:42px 0 48px 0;border:6px solid rgba(255,255,255,.65)}
.service-card-inner{position:absolute;inset:0;border-radius:36px 0 42px 0;background:var(--bright-orange);color:var(--white);text-align:center;padding-top:28px}
.service-card h2{font-weight:400;font-size:20px;line-height:23px}
.service-card h2 strong{font-weight:500}
.service-card p{font-size:10.3px;line-height:15px;margin-top:10px;font-weight:300}
.service-card p+p{margin-top:0}

/* clients */
.hero-snow{left:0;top:0;width:535px;height:460px;background:linear-gradient(180deg,#b9cfe3 0%,#dbe6f0 35%,#eef3f8 70%,#ffffff 100%)}
.newsletter--clients .brand{top:68px;color:var(--navy)}
.newsletter--clients .brand-dot{background:var(--orange)}
.newsletter--clients .headline{top:178px;font-size:38px;color:var(--ink)}
.newsletter--clients .date-pill{left:187px;top:280px;width:180px;height:47px;background:var(--orange);font-size:19px}
.update-icon{position:absolute;left:52px;width:92px;height:92px;border-radius:50%;display:flex;align-items:center;justify-content:center}
.update-item{position:absolute;left:159px;width:350px}
.update-item h3{font-weight:700;font-size:16.5px;color:#111}
.update-item p{margin-top:9px;font-size:12.3px;line-height:18px;color:var(--body)}
.photo-tower{left:0;top:774px;width:535px;height:280px;background:linear-gradient(90deg,#07161f 0%,#0c2333 45%,#1b3e63 75%,#3b6aa0 100%)}
.service-dark{position:absolute;left:58px;top:836px;color:var(--white)}
.service-dark h2{font-weight:400;font-size:22px;line-height:28px}
.service-dark h2 strong{font-weight:500}
.service-dark p{font-size:11px;line-height:14.5px;margin-top:16px;font-weight:400}
</style>
</head>
<body>
<div class="canvas">

  <!-- Prospects newsletter -->
  <section class="newsletter newsletter--prospects">
    <div class="abs hero-dark" role="img" aria-label="Snow-capped mountain range under a deep teal tint"></div>
    <div class="brand"><span class="brand-dot"></span>The Tidegrove</div>
    <h1 class="headline">THE TIDEGROVE<br>NEWSLETTER</h1>
    <div class="date-pill">MARCH 2020</div>

    <div class="abs features-bg" role="img" aria-label="Faded view of city skyscrapers"></div>
    <svg class="abs hero-notch" width="42" height="22" viewBox="0 0 42 22"><polygon points="0,0 42,0 21,20" fill="#195569"/></svg>

    <svg class="feature-pin" style="left:58px;top:397px" width="94" height="110" viewBox="0 0 94 110">
      <circle cx="47" cy="47" r="47" fill="var(--teal)"/><polygon points="35,88 59,88 47,106" fill="var(--teal)"/>
      <g fill="none" stroke="#fff" stroke-width="2" stroke-linecap="round" stroke-linejoin="round">
        <circle cx="52" cy="42" r="15"/><path d="M46,26 h12 l-3,5 h-6z"/>
        <text x="52" y="48" font-family="Roboto,sans-serif" font-size="16" fill="#fff" stroke="none" text-anchor="middle">$</text>
        <path d="M20,60 h10 q10,-4 20,2 h10 q8,-6 12,-4 q-8,10 -22,12 h-20"/><rect x="14" y="56" width="6" height="16"/>
      </g>
    </svg>
    <div class="feature" style="left:30px;top:514px"><h3>INVESTMENT</h3><p>Allamcorper est eget tempor cursus neque mi consect etuer mi a ultricies massa est sed nisl aptent</p></div>

    <svg class="feature-pin" style="left:235px;top:450px" width="94" height="110" viewBox="0 0 94 110">
      <circle cx="47" cy="47" r="47" fill="var(--ink)"/><polygon points="35,88 59,88 47,106" fill="var(--ink)"/>
      <g fill="none" stroke="#fff" stroke-width="2" stroke-linejoin="round">
        <rect x="28" y="56" width="7" height="12"/><rect x="39" y="48" width="7" height="20"/><rect x="50" y="40" width="7" height="28"/><rect x="61" y="32" width="7" height="36"/>
        <path d="M26,48 l16,-12 l8,6 l16,-16" stroke-linecap="round"/><path d="M59,26 h7 v7"/><path d="M24,68 h48"/>
      </g>
    </svg>
    <div class="feature" style="left:207px;top:567px"><h3>GROWTH</h3><p>Allamcorper est eget tempor cursus neque mi consect etuer mi a ultricies massa est sed nisl aptent</p></div>

    <svg class="feature-pin" style="left:411px;top:397px" width="94" height="110" viewBox="0 0 94 110">
      <circle cx="47" cy="47" r="47" fill="var(--teal)"/><polygon points="35,88 59,88 47,106" fill="var(--teal)"/>
      <g fill="none" stroke="#fff" stroke-width="2" stroke-linejoin="round" stroke-linecap="round">
        <circle cx="40" cy="24" r="5"/><path d="M30,52 v-14 q0,-6 10,-6 q10,0 10,6 M34,72 v-24 M46,72 v-18"/>
        <path d="M52,40 l12,5 v10 q0,10 -12,16 q-12,-6 -12,-16 v-10z"/><path d="M47,55 l4,4 l8,-8"/>
      </g>
    </svg>
    <div class="feature" style="left:383px;top:514px"><h3>SECURE WEALTH</h3><p>Allamcorper est eget tempor cursus neque mi consect etuer mi a ultricies massa est sed nisl aptent</p></div>

    <div class="abs photo-field" role="img" aria-label="Couple walking through a sunlit grass field at sunset"></div>
    <div class="abs service-card">
      <div class="service-card-inner">
        <h2>FINANCIAL<br><strong>PLANNING SERVICE</strong></h2>
        <p>Pllamcorper est eget tempor cursus neque mi<br>consectetuer mi a ultricies massa</p>
        <p>Ast sed nisl Class aptent taciti sociosqu ad litora<br>torquent per conubia nostra per incept</p>
      </div>
    </div>
  </section>

  <!-- Clients update -->
  <section class="newsletter newsletter--clients">
    <div class="abs hero-snow" role="img" aria-label="Snowy alpine peaks under a pale blue sky"></div>
    <div class="brand"><span class="brand-dot"></span>The Tidegrove</div>
    <h1 class="headline">THE TIDEGROVE<br>UPDATE</h1>
    <div class="date-pill">MARCH 2020</div>

    <div class="update-icon" style="top:387px;background:var(--navy)">
      <svg width="60" height="60" viewBox="14 14 66 66"><g fill="none" stroke="#fff" stroke-width="2" stroke-linecap="round" stroke-linejoin="round">
        <circle cx="52" cy="42" r="15"/><path d="M46,26 h12 l-3,5 h-6z"/>
        <text x="52" y="48" font-family="Roboto,sans-serif" font-size="16" fill="#fff" stroke="none" text-anchor="middle">$</text>
        <path d="M20,60 h10 q10,-4 20,2 h10 q8,-6 12,-4 q-8,10 -22,12 h-20"/><rect x="14" y="56" width="6" height="16"/></g></svg>
    </div>
    <div class="update-item" style="top:403px"><h3>INVESTMENT</h3><p>Allamcorper est eget tempor cursus neque mi consect etuer mi a ultricies massa est sed nisl aptent</p></div>

    <div class="update-icon" style="top:515px;background:var(--orange)">
      <svg width="60" height="60" viewBox="18 18 60 60"><g fill="none" stroke="#fff" stroke-width="2" stroke-linejoin="round">
        <rect x="28" y="56" width="7" height="12"/><rect x="39" y="48" width="7" height="20"/><rect x="50" y="40" width="7" height="28"/><rect x="61" y="32" width="7" height="36"/>
        <path d="M26,48 l16,-12 l8,6 l16,-16" stroke-linecap="round"/><path d="M59,26 h7 v7"/><path d="M24,68 h48"/></g></svg>
    </div>
    <div class="update-item" style="top:529px"><h3>GROWTH</h3><p>Allamcorper est eget tempor cursus neque mi consect etuer mi a ultricies massa est sed nisl aptent</p></div>

    <div class="update-icon" style="top:638px;background:var(--teal)">
      <svg width="60" height="60" viewBox="18 14 60 62"><g fill="none" stroke="#fff" stroke-width="2" stroke-linejoin="round" stroke-linecap="round">
        <circle cx="40" cy="24" r="5"/><path d="M30,52 v-14 q0,-6 10,-6 q10,0 10,6 M34,72 v-24 M46,72 v-18"/>
        <path d="M52,40 l12,5 v10 q0,10 -12,16 q-12,-6 -12,-16 v-10z"/><path d="M47,55 l4,4 l8,-8"/></g></svg>
    </div>
    <div class="update-item" style="top:652px"><h3>SECURE WEALTH</h3><p>Allamcorper est eget tempor cursus neque mi consect etuer mi a ultricies massa est sed nisl aptent</p></div>

    <div class="abs photo-tower" role="img" aria-label="Glass office tower seen from below against the sky"></div>
    <div class="service-dark">
      <h2>FINANCIAL<br><strong>PLANNING SERVICE</strong></h2>
      <p>Pllamcorper est eget tempor cursus neque mi<br>consectetuer mi a ultricies massa</p>
      <p>sus eu mattis laoreet viverra sit amet quam<br>Curabitur vel dolor ultrices ipsum dictum<br>tristique Praesent vitae lacus</p>
    </div>
  </section>

</div>
</body>
</html>
```